Defense contractor needs a flyer for an exhibition

We need a flyer that we can hand out on an exhibition.
For information about our company and product visit:
https://www.brightmarrowlabs.example/
I have supplied my business card that you can copy the logo and the contact information. the contact information should be on the last page. It would be nice if you would orient on existing publications of my company.

Important:
For designing you must use Adobe Illustrator/Photoshop and the templates provided in the zip file, to guarantee a perfect print. That means also that you have to use CMYK colors.
The flyer has altogether 6 pages by folding. Every side of the 105mm x 210mm paper contains 3 pages. The folding procedure is called "letterfold".

I think CrateView7 and HallwayPlan are the best schematics. They should be somehow included in the flyer.

Target Market(s)

Defense

Industry/Entity Type

Defense

Font styles to use
Serif

Colors
0054AA
0677BA
7BADD7
CADEEF
E8F1F8

Requirements
Must have
• black and blue colors should dominate, the template in the zip files must be used
Nice to have
• I would suggest, that you reuse the picture of the tank in front of the sunset.

```html
<!DOCTYPE html>
<html lang="en">
<head>
<meta charset="utf-8">
<title>Combat Training Systems – Letterfold Flyer</title>
<link rel="stylesheet" href="https://fonts.googleapis.com/css2?family=Montserrat:wght@400;500;600;700&family=Teko:wght@500;600&display=swap">
<style>
:root{
  --page-bg:#e9e9ee;
  --navy-deep:#16193a;
  --navy:#1d2150;
  --indigo:#2b2a6e;
  --violet:#3a2f7e;
  --accent:#2aa8e0;
  --accent-soft:#7badd7;
  --pale:#cadeef;
  --text:#e8f1f8;
}
*{box-sizing:border-box;margin:0;padding:0}
html,body{width:1200px;height:2296px;overflow:hidden;background:var(--page-bg)}
body{font-family:"Montserrat",Arial,sans-serif;color:var(--text);position:relative}
.spread{position:absolute;left:20px;width:1160px;height:782px;overflow:hidden;
  background:linear-gradient(135deg,var(--navy-deep) 0%,var(--indigo) 55%,var(--violet) 100%);
  box-shadow:0 10px 30px rgba(20,20,50,.25)}
.spread--outside{top:336px}
.spread--inside{top:1158px}
.panel{position:absolute;top:0;width:386.67px;height:782px;z-index:2}
.panel--1{left:0}
.panel--2{left:386.67px}
.panel--3{left:773.33px}
.panel--shade{background:linear-gradient(160deg,rgba(10,30,50,.55) 0%,rgba(40,30,100,.2) 60%,rgba(0,0,0,0) 100%)}
.abs{position:absolute}
.grass{position:absolute;left:0;right:0;bottom:0;height:28px;z-index:1;background:linear-gradient(180deg,rgba(10,10,30,0),rgba(8,8,24,.85))}
.art{position:absolute}
.art--photo{z-index:1}
.heading{font-weight:600;color:var(--accent);letter-spacing:.01em}
.section-title{font-size:19px;font-weight:500;letter-spacing:.06em;color:var(--accent)}
.bracket{position:absolute;height:22px;border:1.5px solid var(--accent);border-left:none}
.dots{display:flex;gap:5px}
.dots i{width:5px;height:5px;border-radius:50%;background:var(--accent)}
.dots i:nth-child(2),.dots i:nth-child(4){background:var(--accent-soft)}
.dots i:first-child,.dots i:last-child{opacity:.5}
.body-copy{font-size:11.5px;line-height:1.28;color:var(--text)}
.app-list{list-style:none}
.app-list li{display:flex;align-items:center;gap:14px;height:63px;font-size:14px;font-weight:600;letter-spacing:.04em}
.app-icon{width:46px;height:46px;border-radius:50%;background:var(--accent);display:flex;align-items:center;justify-content:center;box-shadow:0 0 0 3px rgba(42,168,224,.25)}
.contact-title{font-size:25px;font-weight:600;letter-spacing:.06em;text-align:center;color:#fff}
.contact-frame{position:absolute;left:52px;width:282px;height:26px;border:1.5px solid var(--accent);border-bottom:none}
.contact-item{position:absolute;left:0;width:386.67px;text-align:center;font-size:14px;font-weight:500}
.contact-icon{display:block;margin:0 auto 6px;width:28px;height:28px}
.brand{position:absolute;top:60px;right:40px;font-weight:700;font-size:22px;letter-spacing:.04em;color:#fff;text-transform:uppercase;display:flex;align-items:center;gap:8px}
.brand::before{content:"";width:14px;height:14px;background:#fff;display:block}
.cover-title{position:absolute;left:32px;width:330px;white-space:nowrap}
.title-advanced{font-family:"Teko",Impact,sans-serif;font-weight:500;font-size:62px;line-height:1;letter-spacing:.06em;color:var(--accent);text-align:center}
.title-combat{font-family:"Teko",Impact,sans-serif;font-weight:600;font-size:110px;line-height:1;letter-spacing:.02em;color:var(--pale);text-align:center}
.title-systems{font-size:20px;letter-spacing:.36em;color:#fff;font-weight:500}
.title-tagline{font-size:18.5px;font-weight:600;color:var(--accent)}
.web{font-size:18px;font-weight:500;color:#fff;letter-spacing:.01em}
.feature{position:absolute;width:330px}
.feature h4{font-size:12.5px;font-weight:500;color:var(--accent);display:flex;align-items:flex-start;gap:8px;margin-bottom:4px;line-height:1.2}
.feature h4 svg{flex:none}
.feature p{font-size:11.5px;line-height:1.25}
.subhead{font-size:14px;font-weight:600;color:var(--accent);letter-spacing:.02em;margin-bottom:4px}
</style>
</head>
<body>

<section class="spread spread--outside">
  <div class="panel panel--1 panel--shade">
    <h3 class="heading abs" style="left:40px;top:32px;width:320px;font-size:15px;line-height:1.2">VANTIS (Versatile Advanced Network for Training And Instrumentation Systems)</h3>
    <p class="body-copy abs" style="left:40px;top:96px;width:300px">allows for a modern approach to duel simulation, firing range training, armored vehicle driving training, and simulation debriefing through an integrated system of sensors, optics, and controls that give soldiers and instructors real-time, real-world vision and data.</p>
    <h3 class="section-title abs" style="left:40px;top:210px">APPLICATIONS</h3>
    <div class="bracket" style="left:196px;top:220px;width:68px"></div>
    <div class="dots abs" style="left:48px;top:241px"><i></i><i></i><i></i><i></i><i></i></div>
    <ul class="app-list abs" style="left:40px;top:258px">
      <li><span class="app-icon"><svg width="26" height="26" viewBox="0 0 26 26"><rect x="4" y="12" width="18" height="6" rx="2" fill="#fff"/><rect x="8" y="8" width="9" height="5" rx="1" fill="#fff"/><rect x="16" y="9" width="8" height="2" fill="#fff"/></svg></span>DUEL SIMULATION</li>
      <li><span class="app-icon"><svg width="26" height="26" viewBox="0 0 26 26" fill="none" stroke="#fff" stroke-width="2"><circle cx="13" cy="13" r="8"/><circle cx="13" cy="13" r="2.5"/><path d="M13 2v6M13 18v6M2 13h6M18 13h6"/></svg></span>FIRING RANGE TRAINING</li>
      <li><span class="app-icon"><svg width="26" height="26" viewBox="0 0 26 26" fill="none" stroke="#fff" stroke-width="2.4"><circle cx="13" cy="13" r="10"/><path d="M3.5 11h19M13 13v9"/></svg></span>DRIVING TRAINING</li>
      <li><span class="app-icon"><svg width="26" height="26" viewBox="0 0 26 26"><rect x="6" y="4" width="16" height="11" fill="none" stroke="#fff" stroke-width="2"/><circle cx="7" cy="18" r="2.5" fill="#fff"/><rect x="4" y="21" width="6" height="3" fill="#fff"/><circle cx="17" cy="18" r="2.5" fill="#fff"/><rect x="14" y="21" width="6" height="3" fill="#fff"/></svg></span>DEBRIEFING</li>
    </ul>
    <div class="art" role="img" aria-label="Isometric schematic of the CrateView7 instructor command truck" style="left:0;top:540px;width:330px;height:242px;background:linear-gradient(160deg,#d9dce8 0%,#a9aec6 60%,#5a5f8e 100%);opacity:.85;clip-path:polygon(0 30%,60% 0,100% 25%,100% 80%,55% 100%,0 100%)"></div>
  </div>

  <div class="art art--photo" role="img" aria-label="Silhouettes of a soldier and a tank against a purple and orange sunset sky" style="left:386.67px;top:0;width:773.33px;height:456px;background:linear-gradient(180deg,#3c3a88 0%,#7a5aa8 35%,#e38a7a 58%,#5a3f7a 78%,#14152e 100%)"></div>

  <div class="panel panel--2">
    <div class="contact-frame" style="top:442px"></div>
    <h3 class="contact-title abs" style="left:0;width:386.67px;top:432px"><span style="background:var(--navy);padding:0 8px">CONTACT US</span></h3>
    <div class="dots abs" style="left:172px;top:474px"><i></i><i></i><i></i><i></i><i></i></div>
    <div class="contact-item" style="top:498px">
      <svg class="contact-icon" viewBox="0 0 28 28"><circle cx="14" cy="14" r="13" fill="var(--accent)"/><path d="M14 6a5 5 0 0 0-5 5c0 4 5 10 5 10s5-6 5-10a5 5 0 0 0-5-5z" fill="#fff"/><circle cx="14" cy="11" r="2" fill="var(--accent)"/></svg>
      Lindenweg 14 80331<br>Musterstadt Germany
    </div>
    <div class="contact-item" style="top:576px;font-size:15.5px">
      <svg class="contact-icon" viewBox="0 0 28 28"><circle cx="14" cy="14" r="13" fill="var(--accent)"/><path d="M8 11c0-2 2-3 6-3s6 1 6 3l-2 1-1-2h-6l-1 2zM9 13h10v7H9z" fill="#fff"/><circle cx="14" cy="16.5" r="2" fill="var(--accent)"/></svg>
      +49 1570000123
    </div>
    <div class="contact-item" style="top:634px;font-size:12px">
      <svg class="contact-icon" viewBox="0 0 28 28"><circle cx="14" cy="14" r="13" fill="var(--accent)"/><rect x="7" y="9" width="14" height="10" fill="#fff"/><path d="M7 9l7 6 7-6" fill="none" stroke="var(--accent)" stroke-width="1.5"/></svg>
      Jonas.Weller@BrightMarrowLabs.example
    </div>
    <div class="contact-item" style="top:690px;font-size:15px">
      <svg class="contact-icon" viewBox="0 0 28 28"><circle cx="14" cy="14" r="13" fill="var(--accent)"/><g fill="none" stroke="#fff" stroke-width="1.5"><circle cx="14" cy="14" r="7"/><ellipse cx="14" cy="14" rx="3" ry="7"/><path d="M7 14h14"/></g></svg>
      www.BrightMarrowLabs.example
    </div>
  </div>

  <div class="panel panel--3">
    <div class="brand">Bright Marrow Labs</div>
    <div class="cover-title title-advanced" style="top:468px">ADVANCED</div>
    <div class="cover-title title-combat" style="top:528px">COMBAT</div>
    <div class="cover-title title-systems" style="top:630px">TRAINING SYSTEMS</div>
    <div class="cover-title title-tagline" style="top:662px">for Realistic Combat Simulation</div>
    <div class="cover-title dots" style="top:700px;justify-content:center"><i></i><i></i><i></i><i></i><i></i></div>
    <div class="cover-title web" style="top:718px">www.BrightMarrowLabs.example</div>
  </div>
  <div class="grass"></div>
</section>

<section class="spread spread--inside">
  <div class="panel panel--1">
    <div class="art" role="img" aria-label="Isometric schematic of the HallwayPlan instructor classroom with screens and workstations" style="left:50px;top:36px;width:290px;height:204px;background:linear-gradient(160deg,#e3e5ee 0%,#b3b7cc 55%,#6a6e9a 100%);opacity:.85;clip-path:polygon(0 0,100% 0,100% 40%,80% 100%,15% 100%,0 55%)"></div>
    <h3 class="section-title abs" style="left:42px;top:258px;width:340px;line-height:1.2;letter-spacing:.03em">EQUIP YOUR FIGHTING FORCE<br>WITH PRECISION TRAINING</h3>
    <div class="bracket" style="left:300px;top:290px;width:20px;border-top:none"></div>
    <div class="dots abs" style="left:48px;top:318px"><i></i><i></i><i></i><i></i><i></i></div>
    <h4 class="abs" style="left:40px;top:338px;font-size:14px;font-weight:600;color:#fff">Features of VANTIS</h4>
    <p class="body-copy abs" style="left:40px;top:362px;width:312px">Fully deployed in 20 minutes or less, VANTIS is uniquely designed to outfit armored vehicles and weapons systems including MBTs, armored IFVs and more regardless of manufacturer type with an array of advanced sensors and instrumentation for the most realistic and productive combat simulation achievable.</p>
    <div class="feature" style="left:40px;top:494px">
      <h4><svg width="20" height="16" viewBox="0 0 20 16"><rect x="2" y="4" width="16" height="8" rx="2" fill="var(--accent)" transform="rotate(-20 10 8)"/></svg>Remote-Control Functions</h4>
      <p>Remote weapons blocking and camera control for integrated instruction management and safety</p>
    </div>
    <div class="feature" style="left:40px;top:562px">
      <h4><svg width="20" height="16" viewBox="0 0 20 16"><rect x="2" y="3" width="12" height="7" fill="var(--accent)" transform="rotate(-15 8 6)"/><rect x="3" y="11" width="2" height="5" fill="var(--accent)"/></svg>16 Camera Systems per vehicle</h4>
      <p>Supports up to 16 remote-controlled cameras with pan, tilt, zoom, and thermal / night vision compatibility</p>
    </div>
    <div class="feature" style="left:40px;top:632px">
      <h4><svg width="20" height="20" viewBox="0 0 20 20" fill="none" stroke="var(--accent)" stroke-width="2"><circle cx="10" cy="10" r="8"/><circle cx="10" cy="10" r="3"/></svg>Optics Camera</h4>
      <p>Periscope optics camera placement allows for real-time instructor visibility of training grounds, targets, and crew performance</p>
    </div>
  </div>

  <div class="panel panel--2" style="background:linear-gradient(180deg,rgba(20,15,50,.35),rgba(0,0,0,0))">
    <div class="feature" style="left:26px;top:40px">
      <h4><svg width="24" height="20" viewBox="0 0 24 20" fill="var(--accent)"><rect x="2" y="12" width="3" height="8"/><rect x="7" y="8" width="3" height="12"/><rect x="12" y="10" width="3" height="10"/><rect x="17" y="4" width="3" height="16"/></svg>Vehicle Data</h4>
      <p>Lead angles, ammunition types, speed, acceleration, turn indicators, temperature, and positions are shown on an interactive map</p>
    </div>
    <div class="feature" style="left:26px;top:128px">
      <h4><svg width="24" height="20" viewBox="0 0 24 20" fill="none" stroke="var(--accent)" stroke-width="2"><rect x="2" y="2" width="20" height="16" rx="2"/><circle cx="12" cy="10" r="4"/></svg>Full Instructor Overview with Audio, Visuals, Vehicle Data, and Camera Control</h4>
      <p>Live-stream radio, audio, visual, and sensor data overview with camera controls integrated with instructor command vehicle</p>
    </div>
    <div class="feature" style="left:26px;top:232px">
      <h4><svg width="24" height="20" viewBox="0 0 24 20" fill="var(--accent)"><rect x="2" y="2" width="20" height="10" rx="1"/><rect x="5" y="14" width="2" height="5"/><rect x="11" y="14" width="2" height="5"/><rect x="17" y="14" width="2" height="5"/></svg>Air-Conditioned Instructor Command Workstation</h4>
      <p>Instructor workstation comfort control for optimal focus, precision, and command</p>
    </div>
    <div class="feature" style="left:26px;top:310px">
      <h4><svg width="24" height="20" viewBox="0 0 24 20" fill="none" stroke="var(--accent)" stroke-width="2"><rect x="3" y="2" width="16" height="17"/><circle cx="11" cy="12" r="3"/></svg>Full Data Recording</h4>
      <p>Audio, visual, and sensor data for debriefing, archiving, and performance metrics</p>
    </div>
    <div class="feature" style="left:26px;top:376px">
      <h4><svg width="24" height="20" viewBox="0 0 24 20" fill="var(--accent)"><ellipse cx="12" cy="8" rx="9" ry="6"/><rect x="7" y="15" width="2" height="4"/><rect x="14" y="15" width="2" height="4"/></svg>All-Weather and All-Terrain</h4>
      <p>Designed for durability and compatibility in any type of weather or terrain scenario</p>
    </div>
    <h3 class="section-title abs" style="left:28px;top:472px">APPLICATIONS</h3>
    <div class="bracket" style="left:196px;top:482px;width:150px"></div>
    <div class="dots abs" style="left:34px;top:503px"><i></i><i></i><i></i><i></i><i></i></div>
    <div class="abs" style="left:26px;top:528px;width:330px">
      <div class="subhead">DUEL SIMULATION</div>
      <p class="body-copy">VANTIS is designed to surpass laser engagement system capabilities by achieving realistic training environments, hit detection, and soldier assessment and reaction to battle grounds and conditions. Instructors equipped with VANTIS have the advantage of full overview, remote weapons blocking and camera control, and mediation among vehicle teams and units with real-time data delivered across multiple instructor workstations simultaneously for safe real-world training environments and results.</p>
    </div>
  </div>

  <div class="panel panel--3 panel--shade">
    <div class="abs" style="left:24px;top:36px;width:336px">
      <div class="subhead">FIRING RANGE TRAINING</div>
      <p class="body-copy" style="margin-bottom:16px">VANTIS gives instructors complete visual, audio, and data oversight of firing range performance along with camera and weapons blocking control for optimal safety, ammunitions selection and conservation, target precision, and crew instruction.</p>
      <div class="subhead">DRIVING TRAINING</div>
      <p class="body-copy" style="margin-bottom:16px">Vehicle teams with VANTIS have increased vision, awareness, response times, and instructor assistance with control functions during driving training. VANTIS offers cost-effective safety and driving training solutions in both combat and non-combat modes.</p>
      <div class="subhead">DEBRIEFING</div>
      <p class="body-copy">VANTIS equips instructors with comprehensive data collection of training elements allowing for an immersive, insightful, and detailed debriefing process. All data contents can be easily recorded, edited, and archived for reference. VANTIS features mobile container functionality for rapid deployment or a compact stationary workplace.</p>
    </div>
    <div class="art" role="img" aria-label="Isometric schematic of tanks, targets and the CrateView7 command truck on a training range" style="left:10px;top:440px;width:370px;height:320px;background:linear-gradient(160deg,#e3e5ee 0%,#aeb2c8 55%,#5e629a 100%);opacity:.85;clip-path:polygon(40% 0,100% 10%,100% 85%,60% 100%,0 80%,0 35%)"></div>
  </div>
  <div class="grass"></div>
</section>

</body>
</html>
```